WordPress design (BRTK)

We need a wordpress design for an established auction and real estate company based in Viginia- "Don't Pause.... Ascend!". The winning design will incorporate a professional color scheme with company logo in a clean layout.
Industry/Entity Type
Real Estate
Requirements
Must have
- Navigation:
- 1) Home
- 2) Services
- 3) Auctions
- 4) Gala Benefit
- 5) Appraisals
- 6) Past Successes
- 7) About BRTK
- 8) Contact us
- Colors will be those in the attached logo. design should be able to be developed in responsive theme. Wants a "very clean and professional and sharp" design. Site will have slideshow that is relatively small, not a large portion of the design. Please use stock real estate image.
- Footer will have attached logos and contact info for the client.
Nice to have
- A representative drop down menu will be nice to see.

```html
<!DOCTYPE html>
<html lang="en">
<head>
<meta charset="utf-8">
<title>BRTK – Bayridge Realty & Trust Group</title>
<link rel="stylesheet" href="https://fonts.googleapis.com/css2?family=Source+Sans+3:wght@400;600;700&family=Lora:ital@1&display=swap">
<style>
:root{
  --dark:#2a2325;
  --dark-2:#231d1f;
  --page:#f3f3f3;
  --white:#ffffff;
  --red:#c8141c;
  --gold:#e8a93c;
  --price:#e2572a;
  --link:#3d6a8f;
  --text:#4a4a4a;
  --line:#cfcfcf;
  --muted:#bdb8b8;
}
*{box-sizing:border-box;margin:0;padding:0}
html,body{width:1200px;height:1172px;overflow:hidden}
body{background:var(--page);font-family:"Source Sans 3",Arial,sans-serif;color:var(--text);position:relative}
.abs{position:absolute}

.topbar{left:0;top:0;width:1200px;height:52px;background:var(--dark)}
.topbar .call{left:727px;top:13px;color:var(--gold);font-weight:600;font-size:20px}
.topbar .account{left:1018px;top:16px;color:var(--white);font-weight:600;font-size:14px;word-spacing:4px}

.brand{left:42px;top:0;width:268px;height:129px;background:var(--white);box-shadow:0 2px 6px rgba(0,0,0,.35)}
.brand-inner{position:absolute;left:11px;top:12px;width:246px;height:108px;background:var(--dark);color:var(--white);text-align:center}
.brand-inner .mark{position:absolute;left:109px;top:14px;width:28px;height:28px;background:var(--gold)}
.brand-inner .name{position:absolute;left:0;right:0;top:48px;font-size:28px;font-weight:600;letter-spacing:2px}
.brand-inner .sub{position:absolute;left:0;right:0;top:82px;font-size:11px;font-weight:600}

.nav{left:410px;top:89px;display:flex;font-size:16.5px;color:var(--dark);letter-spacing:.5px}
.nav a{color:inherit;text-decoration:none;padding:0 12px 4px}
.nav .sep{color:var(--dark)}
.nav a.active{color:var(--red);border-bottom:2px solid var(--red)}
.nav .caret{color:var(--red);font-size:11px}

.slider{left:105px;top:149px;width:981px;height:330px;background:var(--white);box-shadow:0 1px 5px rgba(0,0,0,.3)}
.slide-photo{left:117px;top:158px;width:638px;height:310px;background:linear-gradient(120deg,#5a3a22 0%,#b88a55 35%,#d9b27a 55%,#8c5a2e 80%,#4a2e1a 100%)}
.slide-arrow{top:296px;color:rgba(255,255,255,.8);font-size:46px;font-weight:300}
.slide-bar{left:117px;top:431px;width:638px;height:37px;background:rgba(0,0,0,.35)}
.dots{left:608px;top:443px;display:flex;gap:11px}
.dots span{width:15px;height:15px;border-radius:50%;background:var(--white)}
.dots span.on{background:var(--dark)}
.slide-info{left:755px;top:158px;width:316px;height:310px;background:var(--dark-2);color:var(--white);overflow:hidden}
.ribbon{position:absolute;left:-34px;top:30px;width:150px;height:32px;background:var(--red);transform:rotate(-45deg);color:var(--white);text-align:center;line-height:32px;font-size:17px;letter-spacing:1px}
.slide-info .desc{position:absolute;left:27px;top:80px;width:262px;font-size:16px;line-height:20px;text-align:justify}
.slide-info .sqft{position:absolute;left:27px;top:158px;font-size:16px}
.slide-info .start{position:absolute;left:27px;top:199px;font-size:21px;color:var(--gold)}
.slide-info .more{position:absolute;left:0;top:273px;width:122px;height:37px;background:#3a3335;text-align:center;line-height:37px;font-size:16px}

.search{left:105px;top:490px;width:981px;height:49px;background:var(--white);display:flex;gap:7px;padding:8px 13px}
.field{height:32px;border:1px solid var(--line);display:flex;justify-content:space-between;align-items:center;font-family:"Lora",serif;font-style:italic;font-size:14px;color:#444;padding-left:10px}
.field .btn{width:38px;height:30px;background:var(--dark);color:var(--white);display:flex;align-items:center;justify-content:center;font-family:"Source Sans 3",sans-serif;font-style:normal;font-weight:600;font-size:18px}

.box{background:var(--white);border:1px solid var(--line)}
.welcome{left:105px;top:556px;width:692px;height:284px;padding:16px 21px}
.welcome h1{font-weight:400;font-size:21px;color:var(--red);letter-spacing:.3px;margin-bottom:14px}
.welcome p{font-size:16px;line-height:20px;text-align:justify;margin-bottom:50px}

.upcoming{left:810px;top:556px;width:276px;height:284px}
.upcoming h2{font-weight:400;font-size:16.5px;color:var(--dark);padding:12px 15px;border-bottom:1px solid var(--line);letter-spacing:.3px}
.prop{display:flex;gap:14px;margin:0 10px;padding:7px 0;border-bottom:1px dotted var(--line)}
.prop:last-child{border-bottom:0}
.thumb{width:85px;height:50px;border:1px solid var(--line);padding:3px;background:var(--white)}
.thumb div{width:100%;height:100%;background:linear-gradient(#9cc0dc 0%,#c9ae86 55%,#5f7a3c 100%)}
.prop .street{font-size:17px;color:var(--link)}
.prop .city{font-family:"Lora",serif;font-style:italic;font-size:13px;color:#777}
.prop .price{font-size:17px;color:var(--price)}

.partners{left:105px;top:854px;width:981px;height:129px;background:var(--white);border:1px solid var(--line)}
.p-arrow{position:absolute;top:0;width:40px;height:127px;background:var(--gold);color:var(--white);font-size:56px;font-weight:300;text-align:center;line-height:120px}
.badge{position:absolute;background:#d9d9d9}

.footer{left:0;top:996px;width:1200px;height:176px;background:var(--dark);color:var(--white)}
.footer h3{position:absolute;top:10px;font-weight:600;font-size:19px;letter-spacing:.3px}
.footer .vline{position:absolute;width:1px;background:#4a4345}
.input{position:absolute;left:42px;width:232px;height:26px;background:#0e0b0c;color:var(--muted);font-size:14px;padding:4px 14px}
.submit{position:absolute;left:184px;top:112px;width:90px;height:26px;background:var(--red);font-weight:600;font-size:16px;text-align:center;line-height:26px}
.quote{position:absolute;left:356px;top:40px;width:262px;font-size:13.5px;line-height:17px;color:var(--muted)}
.byline{position:absolute;left:566px;top:108px;color:var(--gold);font-size:13.5px}
.social{position:absolute;width:24px;height:24px;border-radius:50%;border:2px solid var(--muted)}
.contact{position:absolute;left:971px;top:38px;font-size:13.5px;line-height:17px;color:var(--muted)}
.contact b{color:var(--white);font-weight:600}
.contact .indent{padding-left:62px;display:block}
.copy{position:absolute;left:0;right:0;top:150px;text-align:center;font-size:13.5px;color:var(--muted);border-top:1px solid #3a3335;margin:0 140px;padding-top:4px}
</style>
</head>
<body>

<div class="abs topbar">
  <div class="abs call">CALL ON : (800) 555-01234</div>
  <div class="abs account">LOGIN &nbsp;| &nbsp;SIGN UP</div>
</div>

<div class="abs brand">
  <div class="brand-inner">
    <div class="mark"></div>
    <div class="name">BAYRIDGE</div>
    <div class="sub">REALTY &amp; TRUST GROUP, INC.</div>
  </div>
</div>

<nav class="abs nav">
  <a class="active">HOME</a><span class="sep">|</span>
  <a>ABOUT US</a><span class="sep">|</span>
  <a>PROPERTIES <span class="caret">▼</span></a><span class="sep">|</span>
  <a>AGENTS</a><span class="sep">|</span>
  <a>NEWS</a><span class="sep">|</span>
  <a>CONTACTS</a><span class="sep">|</span>
  <a>DISCLAIMER</a>
</nav>

<div class="abs slider"></div>
<div class="abs slide-photo" role="img" aria-label="Stock photo of a warm-toned tiled bathroom with twin basins and a large mirror"></div>
<div class="abs slide-arrow" style="left:120px">‹</div>
<div class="abs slide-arrow" style="left:724px">›</div>
<div class="abs slide-bar"></div>
<div class="abs dots"><span></span><span></span><span class="on"></span><span></span><span></span></div>
<div class="abs slide-info">
  <div class="ribbon">AUCTION</div>
  <p class="desc">Fusce dictum Viverra ipsum, ut egestas eros egestas non. Aliquam nec diam neque, a egestas sem.</p>
  <p class="sqft">Sqr Feet : 3600</p>
  <p class="start">Start - $ 956,000</p>
  <div class="more">More Info</div>
</div>

<div class="abs search">
  <div class="field" style="width:263px">Find Properties<span class="btn">GO</span></div>
  <div class="field" style="width:220px">Select By Price<span class="btn">▼</span></div>
  <div class="field" style="width:220px">Select By Location<span class="btn">▼</span></div>
  <div class="field" style="width:220px">Select By Type<span class="btn">▼</span></div>
</div>

<section class="abs box welcome">
  <h1>WELCOME TO &nbsp;BAYRIDGE REALTY GROUP</h1>
  <p>Iquam est tortor, sarfisghg, in finagila in, pellesgtang nec erat. Aeneaon semper, neque non faubicus. Iquam est tortor, sarfisghg, in finagila in, pellesgtang nec erat. Aeneaon semper, neque non faubicus.</p>
  <p>Malesuada, dui dfeils tempor feils, vel varius ante diam ut mauris. Aliquam nibh tellus, viverrra ut tristique sed, interdum sed mauris. Malesuada, dui dfeils tempor feils, vel varius ante diam ut mauris. Aliquam nibh tellus, viverrra ut tristique sed, interdum sed mauris</p>
</section>

<aside class="abs box upcoming">
  <h2>UPCOMING PROPERTIES</h2>
  <div class="prop"><div class="thumb"><div role="img" aria-label="Photo of a single-storey house with lawn"></div></div>
    <div><div class="street">318 Maple Road</div><div class="city">Fairview, CA, 95410</div><div class="price">$888,000</div></div></div>
  <div class="prop"><div class="thumb"><div role="img" aria-label="Photo of a two-storey brick house"></div></div>
    <div><div class="street">72 Linden Street</div><div class="city">Fairview, CA, 95410</div><div class="price">$339,000</div></div></div>
  <div class="prop"><div class="thumb"><div role="img" aria-label="Photo of a stone-faced family home"></div></div>
    <div><div class="street">5120 Orchard Court</div><div class="city">Fairview, CA, 95410</div><div class="price">$475,000</div></div></div>
</aside>

<div class="abs partners">
  <div class="p-arrow" style="left:0">‹</div>
  <div class="badge" style="left:53px;top:30px;width:60px;height:65px"></div>
  <div class="badge" style="left:148px;top:30px;width:74px;height:65px"></div>
  <div class="badge" style="left:248px;top:20px;width:140px;height:75px"></div>
  <div class="badge" style="left:410px;top:20px;width:82px;height:80px;border-radius:50%"></div>
  <div class="badge" style="left:516px;top:20px;width:150px;height:75px;background:#2f2f2f"></div>
  <div class="badge" style="left:697px;top:22px;width:120px;height:70px"></div>
  <div class="badge" style="left:848px;top:22px;width:70px;height:75px;border-radius:50% 50% 8px 8px"></div>
  <div class="p-arrow" style="right:0">›</div>
</div>

<footer class="abs footer">
  <h3 style="left:42px">SUBSCRIBE NEWS LETTER</h3>
  <div class="input" style="top:42px">First name</div>
  <div class="input" style="top:77px">Email Id</div>
  <div class="submit">Submit</div>
  <div class="vline" style="left:310px;top:10px;height:104px"></div>

  <h3 style="left:407px">TESTIMONIALS</h3>
  <p class="quote">"Lorem ipsum dolor sit amet, consectetur elit. Pellentesque ut loborts tortor. Duis ut accumsan neque. Morbi iaculis neque eget venenatis"</p>
  <div class="byline">By Mara L.</div>
  <div class="vline" style="left:652px;top:10px;height:104px"></div>

  <h3 style="left:719px">GET IN TOUCH</h3>
  <div class="social" style="left:721px;top:46px"></div>
  <div class="social" style="left:755px;top:46px"></div>
  <div class="social" style="left:788px;top:46px"></div>
  <div class="social" style="left:821px;top:46px"></div>
  <div class="social" style="left:721px;top:79px"></div>
  <div class="social" style="left:755px;top:79px"></div>
  <div class="social" style="left:788px;top:79px"></div>
  <div class="vline" style="left:893px;top:40px;height:104px"></div>

  <h3 style="left:970px">CONTACTS</h3>
  <div class="contact">
    <b>Location :</b> 42 Harbor View Lane,<span class="indent">Elm Crest,</span><span class="indent">Viginia 94310-1120</span>
    <b>Phone :</b> &nbsp;(800) 555-01234<br>
    <b>Mobile :</b> (800) 555-01299<br>
    <b>Email :</b> info@brtk.com
  </div>

  <div class="copy">© &nbsp;2013-2014 BRTK. All Rights Reserved.</div>
</footer>

</body>
</html>
```